Tandle Repair - Handyman and Home Repair Services

I need a business card/letterhead logo for my new handyman service in my local area. I'm happy for a logo design to be done prior to business card design so it can be incorporated on to the card, for which I'd be happy to pay more for. I'd like it to be modern and not using the typical pictures of tools and cartoon characters in dungarees! I like the idea of tools but in a more modern way i.e subtle background images in different shades to main colour. I do like the american retro designs and those that show age and patina for example, having an image half old, half new in its appearance to represent the repairing of things. Colours in mind are 1950's retro colours, ie using grey with pastel greens, red and cream. I'd like to break the mould and the stigma thats attached to these jobs and make it more cool and up to date. I hope this will attract interior designers and more modern businesses to use my services.

This is the logo design I like and would be happy for this idea and colours:

http://toast-a-roam.co.uk/wp-content/uploads/2011/01/t-r_logo600px.png

```html
<!DOCTYPE html>
<html lang="en">
<head>
<meta charset="utf-8">
<title>Tandle Repair – Business Card</title>
<link href="https://fonts.googleapis.com/css2?family=Oswald:wght@500&family=Exo+2:wght@400;500&display=swap" rel="stylesheet">
<style>
  :root {
    --lime: #d4e000;
    --ink: #1c1c1c;
    --charcoal: #3a3a3a;
    --paper: #ffffff;
    --backdrop: #e9e6e1;
    --muted: #4a4a4a;
  }
  * { margin: 0; padding: 0; box-sizing: border-box; }
  html, body { width: 1200px; height: 991px; overflow: hidden; background: var(--backdrop); }
  .stage { position: relative; width: 1200px; height: 991px; }
  .card {
    position: absolute; top: 163px; width: 380px; height: 664px;
    background: var(--paper); overflow: hidden;
    box-shadow: 0 6px 18px rgba(0,0,0,0.18);
  }
  .card--back { left: 190px; }
  .card--front { left: 630px; }
  .card__shapes { position: absolute; inset: 0; width: 100%; height: 100%; }

  .wordmark {
    position: absolute; display: flex; align-items: center; gap: 12px;
    font-family: "Oswald", sans-serif; font-weight: 500; color: var(--ink);
    letter-spacing: 0.5px; white-space: nowrap; line-height: 1;
  }
  .wordmark__square { width: 20px; height: 20px; background: var(--lime); flex: none; }
  .card--back .wordmark { left: 0; right: 0; top: 186px; justify-content: center; font-size: 32px; }
  .card--front .wordmark { left: 36px; top: 222px; font-size: 28px; }

  .tagline {
    position: absolute; left: 36px; top: 260px;
    font-family: "Exo 2", sans-serif; font-weight: 500; font-size: 11px;
    letter-spacing: 0.3px; color: var(--muted); white-space: nowrap;
  }
  .person { position: absolute; left: 36px; top: 318px; }
  .person__name {
    font-family: "Oswald", sans-serif; font-weight: 500; font-size: 30px;
    letter-spacing: 1px; color: var(--ink); line-height: 1.1;
  }
  .person__role {
    font-family: "Oswald", sans-serif; font-weight: 500; font-size: 14px;
    letter-spacing: 2.5px; color: var(--muted); margin-top: 2px;
  }
  .contacts {
    position: absolute; left: 36px; top: 410px; width: 310px;
    display: grid; grid-template-columns: 140px 1fr; row-gap: 16px; column-gap: 14px;
    font-family: "Exo 2", sans-serif; font-size: 11.5px; color: var(--ink);
  }
  .contact { display: flex; align-items: center; gap: 7px; white-space: nowrap; }
  .contact--wide { grid-column: 1 / 3; }
  .contact__icon { width: 18px; height: 18px; flex: none; }
</style>
</head>
<body>
<main class="stage">

  <section class="card card--back" aria-label="Card back">
    <svg class="card__shapes" viewBox="0 0 380 664" aria-hidden="true">
      <path d="M0 560 C120 480 260 430 380 410 V664 H0 Z" fill="var(--charcoal)"/>
      <path d="M0 450 C140 395 270 355 380 330 V395 C250 415 120 460 0 540 Z" fill="var(--lime)"/>
    </svg>
    <div class="wordmark"><span class="wordmark__square"></span>Tandle Repair</div>
  </section>

  <section class="card card--front" aria-label="Card front">
    <svg class="card__shapes" viewBox="0 0 380 664" aria-hidden="true">
      <path d="M150 0 H380 V620 C380 330 310 90 150 0 Z" fill="var(--ink)"/>
      <path d="M300 0 H380 V190 C368 110 342 45 300 0 Z" fill="var(--lime)"/>
    </svg>

    <div class="wordmark"><span class="wordmark__square"></span>Tandle Repair</div>
    <p class="tagline">Handyman and Home Repair Services</p>

    <div class="person">
      <p class="person__name">ALAN MARSH</p>
      <p class="person__role">GENERAL MANAGER</p>
    </div>

    <div class="contacts">
      <p class="contact">
        <svg class="contact__icon" viewBox="0 0 18 18" aria-hidden="true"><circle cx="9" cy="9" r="8" fill="none" stroke="var(--ink)" stroke-width="1.2"/><path d="M6 5 L7.5 5 L8 7 L7 7.8 C7.6 9 8.6 10 9.8 10.6 L10.6 9.6 L12.6 10.1 L12.6 11.6 C9 12 5.6 8.6 6 5 Z" fill="var(--ink)"/></svg>
        014 552 7310
      </p>
      <p class="contact">
        <svg class="contact__icon" viewBox="0 0 18 18" aria-hidden="true"><circle cx="9" cy="9" r="8" fill="none" stroke="var(--ink)" stroke-width="1.2"/><rect x="5" y="6" width="8" height="6" rx="1" fill="var(--ink)"/><path d="M5.3 6.3 L9 9 L12.7 6.3" fill="none" stroke="var(--paper)" stroke-width="0.9"/></svg>
        hello@tandlerepair.com
      </p>
      <p class="contact">
        <svg class="contact__icon" viewBox="0 0 18 18" aria-hidden="true"><circle cx="9" cy="9" r="8" fill="none" stroke="var(--ink)" stroke-width="1.2"/><rect x="6.5" y="4.5" width="5" height="9" rx="1" fill="none" stroke="var(--ink)" stroke-width="1.2"/><circle cx="9" cy="11.7" r="0.6" fill="var(--ink)"/></svg>
        014 552 7310
      </p>
      <p class="contact">
        <svg class="contact__icon" viewBox="0 0 18 18" aria-hidden="true"><circle cx="9" cy="9" r="8" fill="none" stroke="var(--ink)" stroke-width="1.2"/><circle cx="9" cy="9" r="4.5" fill="none" stroke="var(--ink)" stroke-width="1"/><path d="M4.5 9 H13.5 M9 4.5 V13.5" stroke="var(--ink)" stroke-width="0.8"/></svg>
        www.tandlerepair.com
      </p>
      <p class="contact contact--wide">
        <svg class="contact__icon" viewBox="0 0 18 18" aria-hidden="true"><circle cx="9" cy="9" r="8" fill="none" stroke="var(--ink)" stroke-width="1.2"/><path d="M9 14 C7 11 5.8 9.4 5.8 7.6 A3.2 3.2 0 0 1 12.2 7.6 C12.2 9.4 11 11 9 14 Z" fill="var(--ink)"/><circle cx="9" cy="7.6" r="1.2" fill="var(--paper)"/></svg>
        42 Elmfield Road, Unit 3, Harbourside
      </p>
    </div>
  </section>

</main>
</body>
</html>
```